New Website design for VelvetCrate.com - A Monthly Subscription Sexy Lingerie Biz

Look at these sites: https://www.quillrazorguild.com; http://www.parcelwardrobe.com; http://www.tinyfernpack.com; https://www.ochreladle.com; https://thegoldenradish.com; http://www.petalwickcrate.com; https://wagtote.com; https://www.marlowehush.com/coral

Industry/Entity Type

Lingerie

Coding

Coded - Design and coding required

Number of Pages Required

1 page

```html
<!DOCTYPE html>
<html lang="en">
<head>
<meta charset="utf-8">
<title>VelvetCrate — Intimate Underwear</title>
<link href="https://fonts.googleapis.com/css2?family=Montserrat:wght@400;500;600;700&display=swap" rel="stylesheet">
<style>
  :root {
    --violet: #9c4ff2;
    --violet-deep: #8a3de6;
    --violet-soft: #b57bf7;
    --hero-top: #a760f6;
    --hero-bottom: #9a4ef0;
    --ink: #3a3a44;
    --muted: #a9a9b3;
    --panel: #f7f8fa;
    --card: #f4f5f8;
    --white: #ffffff;
  }
  * { margin: 0; padding: 0; box-sizing: border-box; }
  html, body { width: 1200px; height: 2416px; overflow: hidden; }
  body {
    position: relative;
    background: var(--white);
    font-family: "Montserrat", Arial, sans-serif;
    color: var(--ink);
  }
  .abs { position: absolute; }

  /* Hero */
  .hero { position: absolute; left: 0; top: 0; width: 1200px; height: 612px; overflow: hidden; }
  .hero-photo {
    position: absolute; inset: 0;
    background:
      radial-gradient(ellipse 420px 260px at 520px 420px, rgba(255,255,255,0.10), transparent 70%),
      radial-gradient(ellipse 300px 200px at 850px 180px, rgba(255,255,255,0.08), transparent 70%),
      linear-gradient(180deg, var(--hero-top), var(--hero-bottom));
  }
  .brand {
    position: absolute; left: 243px; top: 20px;
    color: var(--white); font-weight: 700; font-size: 18px; letter-spacing: 0.5px;
  }
  .nav { position: absolute; top: 24px; left: 511px; display: flex; align-items: center; gap: 0; }
  .nav a {
    color: var(--white); text-decoration: none; font-size: 11px; font-weight: 500;
    margin-right: 18px; white-space: nowrap;
  }
  .nav svg { margin-left: 6px; margin-right: 10px; }
  .hero-title {
    position: absolute; left: 0; width: 1200px; top: 238px; text-align: center;
    color: var(--white); font-weight: 600; font-size: 30px; letter-spacing: 0.5px;
  }
  .hero-lead {
    position: absolute; left: 0; width: 1200px; top: 284px; text-align: center;
    color: var(--white); font-size: 14.5px; line-height: 21px; font-weight: 500;
  }
  .btn-outline {
    position: absolute; left: 523px; top: 343px; width: 156px; height: 31px;
    border: 2px solid var(--white); border-radius: 16px;
    color: var(--white); font-size: 11px; font-weight: 600; letter-spacing: 0.5px;
    display: flex; align-items: center; justify-content: center;
  }

  /* Subscribe forms */
  .subscribe {
    position: absolute; height: 31px; border-radius: 16px; display: flex; overflow: hidden;
    font-size: 11px; font-weight: 600; letter-spacing: 0.5px;
  }
  .subscribe .field { flex: 1; display: flex; align-items: center; padding-left: 18px; }
  .subscribe .action { display: flex; align-items: center; justify-content: center; border-radius: 16px; }
  .subscribe--light { left: 430px; top: 652px; width: 338px; border: 1.5px solid var(--violet); }
  .subscribe--light .field { color: var(--violet); font-weight: 500; }
  .subscribe--light .action { width: 156px; background: var(--violet); color: var(--white); }
  .subscribe--dark { left: 446px; top: 2204px; width: 339px; border: 1.5px solid var(--white); }
  .subscribe--dark .field { color: var(--white); }
  .subscribe--dark .action { width: 156px; background: var(--white); color: #6d6d78; font-weight: 500; }

  /* Features */
  .features { position: absolute; left: 0; top: 720px; width: 1200px; height: 561px; background: var(--panel);
    box-shadow: inset 0 6px 8px -6px rgba(0,0,0,0.08); }
  .feature { position: absolute; width: 200px; text-align: center; }
  .feature svg { display: block; margin: 0 auto; }
  .feature h3 { font-size: 14px; font-weight: 500; letter-spacing: 0.5px; margin-top: 10px; color: var(--ink); }
  .feature p { font-size: 11px; line-height: 13px; color: var(--muted); margin-top: 8px; }
  .feature-photo { position: absolute; border-radius: 40px; }

  /* Products */
  .section-title { position: absolute; left: 0; width: 1200px; top: 1336px; text-align: center;
    font-size: 19px; font-weight: 500; letter-spacing: 1px; color: var(--ink); }
  .product { position: absolute; width: 160px; text-align: center; }
  .product .card { height: 248px; background: var(--card); border-radius: 4px; position: relative; }
  .product .shot { position: absolute; left: 22px; right: 22px; border-radius: 30px; }
  .product .shot.top { top: 22px; height: 96px; }
  .product .shot.bottom { top: 148px; height: 80px; border-radius: 20px 20px 60px 60px; }
  .product .name { font-size: 9px; color: var(--muted); margin-top: 10px; }
  .product .price { font-size: 11.5px; color: var(--violet); font-weight: 500; margin-top: 3px; }

  /* Footer */
  .signup-band { position: absolute; left: 0; top: 2070px; width: 1200px; height: 282px;
    background:
      radial-gradient(ellipse 360px 200px at 760px 150px, rgba(120,40,200,0.25), transparent 70%),
      linear-gradient(180deg, #a45cf6, #9c50f2); }
  .footer { position: absolute; left: 0; top: 2352px; width: 1200px; height: 64px; background: var(--panel); }
  .copyright { position: absolute; left: 243px; top: 26px; font-size: 10.5px; color: var(--muted); }
  .social { position: absolute; left: 997px; top: 25px; display: flex; gap: 18px; }
  .social span { width: 14px; height: 14px; border-radius: 50%; background: #3a3a44; display: block; }
</style>
</head>
<body>

<header class="hero">
  <div class="hero-photo" role="img" aria-label="Model in lace lingerie lying on a bed, under a violet tint"></div>
  <div class="brand">VELVETCRATE</div>
  <nav class="nav">
    <a>New Arrivals</a><a>Bras</a><a>Panties</a><a>Vanishing Dresses</a><a>Loungewear</a><a>Sale</a>
    <svg width="13" height="12" viewBox="0 0 13 12" fill="none" stroke="#fff" stroke-width="1.2"><path d="M0.5 1h2l1.6 7h6.6l1.6-5H3.4"/><circle cx="5" cy="10.5" r="0.9"/><circle cx="10" cy="10.5" r="0.9"/></svg>
    <svg width="12" height="12" viewBox="0 0 12 12" fill="none" stroke="#fff" stroke-width="1.3"><circle cx="5" cy="5" r="3.8"/><path d="M8 8l3.3 3.3"/></svg>
  </nav>
  <h1 class="hero-title">INTIMATE UNDERWEAR</h1>
  <p class="hero-lead">Our promise is to fit you with the best size and style of bra that<br>fitsand flatters your shape.</p>
  <div class="btn-outline">SHOP NOW</div>
</header>

<form class="subscribe subscribe--light">
  <span class="field">EMAIL</span><span class="action">SUBSCRIBE</span>
</form>

<section class="features">
  <div class="feature" style="left:240px; top:55px;">
    <svg width="52" height="66" viewBox="0 0 52 66" fill="none" stroke="#9c4ff2" stroke-width="2" stroke-linejoin="round">
      <path d="M26 2l5 4 6-1 2 6 6 3-2 6 3 5-5 4v6l-6 2-3 5-6-2-6 2-3-5-6-2v-6l-5-4 3-5-2-6 6-3 2-6 6 1z"/>
      <circle cx="26" cy="25" r="11"/>
      <path d="M15 45v19l11-6 11 6V45"/>
    </svg>
    <h3>BEST QUALITY</h3>
    <p>Lorem ipsum dolor sit amet,<br>consectetur adipisicing elit, sed<br>do eiusmod tempor<br>incididunt.</p>
  </div>
  <div class="feature" style="left:755px; top:63px;">
    <svg width="50" height="50" viewBox="0 0 50 50" fill="none" stroke="#9c4ff2" stroke-width="2">
      <circle cx="25" cy="25" r="6"/>
      <ellipse cx="25" cy="10" rx="7" ry="9"/><ellipse cx="25" cy="40" rx="7" ry="9"/>
      <ellipse cx="10" cy="25" rx="9" ry="7"/><ellipse cx="40" cy="25" rx="9" ry="7"/>
    </svg>
    <h3 style="margin-top:18px">NATURAL MATERIAL</h3>
    <p>Lorem ipsum dolor sit amet,<br>consectetur adipisicing elit, sed<br>do eiusmod tempor<br>incididunt.</p>
  </div>
  <div class="feature" style="left:240px; top:346px;">
    <svg width="62" height="62" viewBox="0 0 62 62" fill="none" stroke="#9c4ff2" stroke-width="2" stroke-linejoin="round">
      <path d="M36 3h22v22L25 58 3 36z"/><circle cx="48" cy="13" r="3.5"/>
      <path d="M18 34l12-12M22 40l9-9"/>
    </svg>
    <h3>BEST PRICE</h3>
    <p>Lorem ipsum dolor sit amet,<br>consectetur adipisicing elit, sed<br>do eiusmod tempor<br>incididunt.</p>
  </div>
  <div class="feature" style="left:755px; top:348px;">
    <svg width="42" height="50" viewBox="0 0 42 50" fill="none" stroke="#9c4ff2" stroke-width="2" stroke-linejoin="round">
      <path d="M7 2v10M35 2v10M3 22c2-8 6-10 10-10s6 4 8 6c2-2 4-6 8-6s8 2 10 10z"/>
      <path d="M3 32h36M3 32c6 3 10 8 12 16h12c2-8 6-13 12-16"/>
    </svg>
    <h3 style="margin-top:13px">UNIQUE DESIGN</h3>
    <p>Lorem ipsum dolor sit amet,<br>consectetur adipisicing elit, sed<br>do eiusmod tempor<br>incididunt.</p>
  </div>
  <div class="feature-photo" role="img" aria-label="Violet lace padded bra"
       style="left:503px; top:69px; width:201px; height:173px; background:radial-gradient(ellipse at 50% 65%, #9a48e8 0%, #b37af3 60%, rgba(247,248,250,0) 100%);"></div>
  <div class="feature-photo" role="img" aria-label="Matching violet lace thong"
       style="left:503px; top:295px; width:201px; height:126px; border-radius:30px 30px 90px 90px; background:radial-gradient(ellipse at 50% 40%, #9a48e8 0%, #b37af3 60%, rgba(247,248,250,0) 100%);"></div>
</section>

<h2 class="section-title">POPULAR PRODUCTS</h2>

<div class="product" style="left:245px; top:1416px;"><div class="card">
  <div class="shot top" role="img" aria-label="Lilac lace bra" style="background:#7b62e6"></div>
  <div class="shot bottom" role="img" aria-label="Lilac lace briefs" style="background:#7b62e6"></div></div>
  <p class="name">Sexy padded low plunge U bra</p><p class="price">£28.00</p></div>
<div class="product" style="left:427px; top:1416px;"><div class="card">
  <div class="shot top" role="img" aria-label="Blue lace bra" style="background:#2fa9d8"></div>
  <div class="shot bottom" role="img" aria-label="Blue lace briefs" style="background:#2fa9d8"></div></div>
  <p class="name">Sexy padded low plunge U bra</p><p class="price">£28.00</p></div>
<div class="product" style="left:614px; top:1416px;"><div class="card">
  <div class="shot top" role="img" aria-label="Magenta lace bra" style="background:#a93bc9"></div>
  <div class="shot bottom" role="img" aria-label="Magenta lace briefs" style="background:#a93bc9"></div></div>
  <p class="name">Sexy padded low plunge U bra</p><p class="price">£28.00</p></div>
<div class="product" style="left:797px; top:1416px;"><div class="card">
  <div class="shot top" role="img" aria-label="Orange lace bra" style="background:#fba523"></div>
  <div class="shot bottom" role="img" aria-label="Orange lace briefs" style="background:#fba523"></div></div>
  <p class="name">Sexy padded low plunge U bra</p><p class="price">£28.00</p></div>

<div class="product" style="left:245px; top:1720px;"><div class="card">
  <div class="shot top" role="img" aria-label="Green lace bra" style="background:#55d83f"></div>
  <div class="shot bottom" role="img" aria-label="Green lace briefs" style="background:#55d83f"></div></div>
  <p class="name">Sexy padded low plunge U bra</p><p class="price">£28.00</p></div>
<div class="product" style="left:427px; top:1720px;"><div class="card">
  <div class="shot top" role="img" aria-label="Lime lace bra" style="background:#bff41a"></div>
  <div class="shot bottom" role="img" aria-label="Lime lace briefs" style="background:#bff41a"></div></div>
  <p class="name">Sexy padded low plunge U bra</p><p class="price">£28.00</p></div>
<div class="product" style="left:614px; top:1720px;"><div class="card">
  <div class="shot top" role="img" aria-label="Red lace bra" style="background:#f2231c"></div>
  <div class="shot bottom" role="img" aria-label="Red lace briefs" style="background:#f2231c"></div></div>
  <p class="name">Sexy padded low plunge U bra</p><p class="price">£28.00</p></div>
<div class="product" style="left:797px; top:1720px;"><div class="card">
  <div class="shot top" role="img" aria-label="Cyan lace bra" style="background:#2dc7ec"></div>
  <div class="shot bottom" role="img" aria-label="Cyan lace briefs" style="background:#2dc7ec"></div></div>
  <p class="name">Sexy padded low plunge U bra</p><p class="price">£28.00</p></div>

<section class="signup-band" role="img" aria-label="Close-up of lingerie on a bed, under a violet tint"></section>
<form class="subscribe subscribe--dark">
  <span class="field">EMAIL</span><span class="action">SUBSCRIBE</span>
</form>

<footer class="footer">
  <p class="copyright">©2016 ·VelvetCrate.</p>
  <div class="social"><span></span><span></span><span></span></div>
</footer>

</body>
</html>
```